依頼詳細
プロが業務用の高圧洗浄機を使い、ご自宅の外構・駐車場(ガレージ)・ブロック塀・玄関タイル・を綺麗にされたい方を募集します。
泥、排気ガスの汚れ、コケ、ほこり等を綺麗に致します。
お見積りは無料
高圧洗浄専門店
割引制度有
平日割引あり(火曜日・水曜日は特別料金にて実施)(空き状況はお電話にてご確認下さい)
施工料金等、丁寧に分かりやすくご説明します。
作業時間平均:2時間~3時間
料金:33,000円~
作業時:水道をお借りします
まずは、お気軽にご相談下さい。
株式会社ミドリノハウジング
TEL:094ー318-5562
担当:坂巻(さかまき)・梅沢(うめざわ)
営業時間:9:00~19:00

記載項目
株式会社ミドリノハウジング
094-318-5562
料金:33,000円~(範囲によって異なります)
プロの高圧洗浄はミドリノハウジングにお任せください。
サイズ
A4
ページ数
片面
希望イメージ
シンプル 複雑
単色 カラフル
暗い 明るい
日常 高級
遊び心 厳粛
未来的 伝統的
女性的 男性的
希望する色
水色系、ターコイズブルーの使用をお願い致します。
納品ファイル
• 高解像度JPG (.jpg)
補足説明
会社ロゴを添付しておりますので、ロゴの使用をお願い致します。
■ 選んだ理由

見やすく、弊社希望のチラシに近いものでした。
頂きました案件全てのチラシ案を印刷し、三つ折りにしましたが、一番良かったです。
伝えたい内容も、しっかり入っており、戸建てとなると年配の方が多いと思われ、その点でも大事な部分は文字が大きく見やすさも良く選ばせて頂きました。

■ 提案者全員のお礼・コメント

初めての依頼となりましたが、多数の応募を頂きましてありがとうございました。
正直、こんなに多数の応募を頂けるとは思ってませんでしたので驚きました。
今後もチラシの案をご依頼する事もるかと思いますので、宜しくお願い致します。

```html
<!DOCTYPE html>
<html lang="ja">
<head>
<meta charset="utf-8">
<title>高圧 外構洗浄 平日格安プラン | ミドリノハウジング</title>
<link href="https://fonts.googleapis.com/css2?family=Noto+Sans+JP:wght@400;500;700;900&display=swap" rel="stylesheet">
<style>
:root{
  --turquoise:#14a3d6;
  --blue-deep:#0c6fb3;
  --navy:#0b3f6e;
  --red:#e5141b;
  --yellow:#fff200;
  --ink:#111;
  --white:#fff;
  --paper:#ffffff;
}
*{margin:0;padding:0;box-sizing:border-box}
html,body{width:846px;height:1200px;overflow:hidden;background:var(--paper)}
body{font-family:"Noto Sans JP",sans-serif;color:var(--ink);position:relative}
.scene{position:absolute;left:0;top:0;width:846px;height:1020px;
  background:linear-gradient(180deg,#bfe3f5 0%,#e9f4f0 14%,#9fc08a 26%,#6f8f63 34%,#8d8f86 42%,#b8b6ae 55%,#7b7a72 70%,#4d5f66 100%)}
.washed-wall{position:absolute;left:0;top:395px;width:846px;height:270px;
  background:linear-gradient(90deg,#9a9890 0%,#c9c7bf 45%,#e6e3da 70%,#a8a59c 100%);opacity:.75}
.badge-kouatsu{position:absolute;left:28px;top:22px;width:150px;height:86px;border-radius:43px;
  background:var(--blue-deep);color:var(--white);font-weight:900;font-size:56px;
  display:flex;align-items:center;justify-content:center;letter-spacing:2px;border:4px solid var(--white)}
.title-main{position:absolute;left:190px;top:12px;width:620px;height:100px;background:var(--turquoise);
  color:var(--white);font-weight:900;font-size:92px;line-height:92px;text-align:center;letter-spacing:8px;
  border:4px solid var(--white)}
.headline{position:absolute;left:0;width:846px;top:118px;text-align:center;font-weight:900;font-size:60px;line-height:1.3;
  color:var(--ink);text-shadow:0 0 6px #fff,0 0 6px #fff,0 0 10px #fff}
.headline .accent{color:var(--red)}
.duration{position:absolute;left:50px;top:200px;width:130px;height:86px;background:var(--blue-deep);
  color:var(--white);font-weight:700;font-size:18px;line-height:1.25;text-align:center;padding-top:6px;border-radius:6px}
.duration b{font-size:20px}
.price{position:absolute;left:190px;top:180px;font-weight:900;font-size:126px;line-height:1.2;color:var(--red);letter-spacing:-3px;
  text-shadow:4px 0 #fff,-4px 0 #fff,0 4px #fff,0 -4px #fff,3px 3px #fff,-3px -3px #fff,3px -3px #fff,-3px 3px #fff}
.price .yen{font-size:84px}
.tax{position:absolute;left:756px;top:198px;font-weight:900;font-size:22px;color:var(--ink);text-shadow:0 0 4px #fff,0 0 4px #fff}
.special{position:absolute;left:430px;top:330px;width:378px;height:58px;background:var(--turquoise);
  color:var(--yellow);font-weight:900;font-size:38px;line-height:52px;text-align:center;border:3px solid var(--white)}
.free-estimate{position:absolute;left:662px;top:530px;width:160px;height:125px;border-radius:50%;background:var(--red);
  color:var(--white);font-weight:900;text-align:center;display:flex;flex-direction:column;justify-content:center;border:4px solid var(--white)}
.free-estimate .small{font-size:26px}
.free-estimate .big{font-size:44px;color:var(--yellow);line-height:1.05}
.service-copy{position:absolute;left:0;top:665px;width:846px;height:78px;background:rgba(11,63,110,.55);
  color:var(--white);font-weight:700;font-size:19px;line-height:1.6;padding:6px 34px}
.service-copy .hl{color:var(--yellow)}
.pro-band{position:absolute;left:0;top:743px;width:846px;height:56px;background:var(--white);
  font-weight:900;font-size:27px;line-height:56px;text-align:center;color:var(--blue-deep);white-space:nowrap}
.pro-band .red{color:var(--red)}
.before-after{position:absolute;left:36px;top:808px;width:420px;height:200px;display:grid;grid-template-columns:1fr 1fr;gap:8px}
.before-after div{border:3px solid var(--white)}
.ph-before{background:linear-gradient(160deg,#6b6a5e,#4a4a40)}
.ph-after{background:linear-gradient(160deg,#d9d5c8,#aeaa9c)}
.notes{position:absolute;left:470px;top:830px;width:210px;background:rgba(255,255,255,.9);padding:10px 12px;
  font-size:14px;font-weight:700;line-height:1.7;color:var(--navy);border-radius:6px}
.worker{position:absolute;left:690px;top:806px;width:130px;height:206px;background:linear-gradient(180deg,#f3e7d6,#6a8fb0);border-radius:8px}
.footer{position:absolute;left:0;top:1020px;width:846px;height:180px;background:var(--paper);border-top:6px solid var(--turquoise)}
.brand{position:absolute;left:30px;top:26px;width:200px;text-align:center}
.brand .tag{display:block;font-size:14px;font-weight:700;color:var(--blue-deep)}
.brand .mark{display:inline-block;width:30px;height:30px;background:var(--turquoise);margin:8px 0}
.brand .name{display:block;font-size:20px;font-weight:900;color:var(--blue-deep)}
.contact{position:absolute;left:250px;top:10px;width:580px}
.contact .lead{font-size:15px;font-weight:700;line-height:1.45}
.contact .company{font-size:26px;font-weight:900;color:var(--navy);line-height:1.35;margin-top:2px}
.contact .addr{font-size:11px;color:#333;line-height:1.4}
.tel{position:absolute;left:250px;top:114px;display:flex;align-items:center;gap:6px;font-weight:900;font-size:36px;line-height:1.2;color:var(--turquoise)}
.staff{position:absolute;left:580px;top:120px;font-size:13px;font-weight:700;line-height:1.5;color:#222}
</style>
</head>
<body>
<div class="scene" role="img" aria-label="戸建て住宅の外構と植栽、空を背景にした写真"></div>
<div class="washed-wall" role="img" aria-label="ブロック塀を高圧洗浄機で洗浄している写真"></div>

<div class="badge-kouatsu">高圧</div>
<h1 class="title-main">外構洗浄</h1>
<p class="headline">平日<span class="accent">格安</span>プラン実施中!</p>

<div class="duration">作業時間<br>平均<br><b>2~3時間</b></div>
<p class="price">33,000<span class="yen">円~</span></p>
<p class="tax">税込</p>
<p class="special">火曜・水曜特別料金</p>

<div class="free-estimate"><span class="small">お見積り</span><span class="big">無料</span></div>

<p class="service-copy"><span class="hl">業務用の高圧洗浄機</span>を使い、ご自宅の外構・駐車場(ガレージ)・ブロック塀・玄関タイルの泥、排気ガスの汚れ、コケ、ほこり等を綺麗に致します。</p>
<p class="pro-band">プロによる<span class="red">高圧洗浄</span>はミドリノハウジングにお任せください!</p>

<div class="before-after">
  <div class="ph-before" role="img" aria-label="洗浄前の汚れた床面の写真"></div>
  <div class="ph-after" role="img" aria-label="洗浄後の綺麗になった床面の写真"></div>
</div>
<div class="notes">※割引制度有<br>※空き状況はお電話にてご確認下さい<br>※作業時は水道をお借りします</div>
<div class="worker" role="img" aria-label="高圧洗浄機を持つ作業員のイラスト"></div>

<footer class="footer">
  <div class="brand">
    <span class="tag">高圧洗浄専門店</span>
    <span class="mark"></span>
    <span class="name">ミドリノハウジング</span>
  </div>
  <div class="contact">
    <p class="lead">施工料金等、丁寧に分かりやすくご説明しますので<br>まずは、お気軽にお問い合わせ・ご相談ください!</p>
    <p class="company">株式会社ミドリノハウジング</p>
    <p class="addr">〒802-0006 北九州市小倉北区緑町2-8-14 ミドリノビル3F</p>
  </div>
  <div class="tel">
    <svg width="32" height="32" viewBox="0 0 24 24" aria-hidden="true"><path fill="#14a3d6" d="M6.6 10.8a15.1 15.1 0 0 0 6.6 6.6l2.2-2.2c.3-.3.7-.4 1-.2 1.1.4 2.3.6 3.6.6.6 0 1 .4 1 1V20c0 .6-.4 1-1 1A17 17 0 0 1 3 4c0-.6.4-1 1-1h3.5c.6 0 1 .4 1 1 0 1.3.2 2.5.6 3.6.1.3 0 .7-.2 1z"/></svg>
    094-318-5562
  </div>
  <p class="staff">営業時間 9:00~19:00<br>担当:坂巻(さかまき)・梅沢(うめざわ)</p>
</footer>
</body>
</html>
```